Due to client commitments, we don't have time in-house to complete this project...
We need a design refresh for our web company! It's time for us to move things along, so we're looking to PixelGuild to get this done!
Our clients tend to be associations and government, with some element of business clients. We need a design that appeals to this sophisticated target market.
Our current web site can be found at www.brindlecove.ca. We are looking for a more personable, contemporary look for the new site design. However, you can see our logo on this site, and some of the content.
The design you provide will be implemented in Lumen. The design winner will only need to provide the PSD or Fireworks PNG format. We anticipate creating the template coding in-house.
However, if you have experience creating Lumen templates, please let us know as we may ask you to bid separately to do that phase of the project.
We've provided you with wireframes of the home page and the inside page, along with Adobe Illustrator and PSD versions of our logo.
For the home page, we've indicated that we'd like to have a slider implemented into the design. For the purpose of design, we believe we'll use this slider: http://demo.tallowforge.com/breezy-fanfold-carousel.html.
The slider will contain inspiration photos related to each of the tabs. Ideally, we would like you to suggest the images for the slider. The dimension of the slider can be adjusted. We would like more space for the image with less for the text. The slider height should be sufficient to ensure the image "stimulates" the audience and sets the tone for the landing page.
The wireframe is provided to illustrate the placement of content and menu items. The exact dimensions of each component can be revised as you see fit.
Our clients tend to be associations, non-profit, government, and business clients. We need a design that appeals to this sophisticated target market.
Business

```html
<!DOCTYPE html>
<html lang="en">
<head>
<meta charset="utf-8">
<title>Brindlecove Communications</title>
<link href="https://fonts.googleapis.com/css2?family=Open+Sans:wght@400;600;700&family=Arimo:wght@400;700&display=swap" rel="stylesheet">
<style>
:root{
  --ink:#222;
  --topbar:#2a2a2a;
  --dark:#4a4a4a;
  --orange:#f4620f;
  --orange-text:#f15a0c;
  --paper:#e3e3e0;
  --lower:#d3d3cf;
  --white:#fff;
  --blogbox:#cdcdc8;
  --muted:#666;
  --line:#e2e2e2;
}
*{box-sizing:border-box;margin:0;padding:0}
html,body{width:906px;height:1200px;overflow:hidden}
body{position:relative;background:var(--lower);font-family:Arimo,Arial,sans-serif;color:var(--ink)}
.abs{position:absolute}
.topbar{left:0;top:0;width:906px;height:19px;background:var(--topbar);color:#f0a020;font-size:11px}
.topbar span{position:absolute;top:3px}
.topbar .phone{color:#fff;font-weight:700;font-size:12px;top:2px}
.header{left:0;top:19px;width:906px;height:112px;background:var(--paper)}
.logo{left:70px;top:38px;display:flex;align-items:center;gap:8px}
.logo-mark{width:52px;height:52px;border-radius:50%;background:var(--orange)}
.logo-name{font-family:"Open Sans",sans-serif;font-weight:700;font-size:17px;color:#333;line-height:1.1}
.quote{left:697px;top:25px;width:152px;height:46px;border-radius:6px;background:linear-gradient(#f4f4f4,#cfcfcf);box-shadow:0 2px 3px rgba(0,0,0,.35);display:flex;align-items:center;gap:8px;padding-left:10px;font:700 15px "Open Sans",sans-serif;color:#174f7a}
.quote i{width:28px;height:28px;border-radius:50%;background:#2a6e9e;color:#fff;font-style:normal;text-align:center;line-height:28px;font-size:18px}
.social{top:79px;width:17px;height:17px;background:#3d6fb3;border-radius:2px}
.nav{left:55px;top:102px;width:799px;height:42px;background:var(--dark);border-radius:8px;color:#fff;font-size:13px;z-index:2}
.nav span{position:absolute;top:13px}
.nav .on{color:#f7941d}
.band{left:0;top:131px;width:906px;height:327px;background:repeating-linear-gradient(135deg,#f4620f 0 6px,#f06010 6px 12px)}
.tab{top:162px;height:24px;background:var(--white);border-radius:8px 8px 0 0;font-size:13px;color:var(--orange-text);text-align:center;line-height:24px}
.tab.on{color:#333}
.stage{left:56px;top:184px;width:795px;height:366px;background:var(--white);border-radius:6px;box-shadow:0 4px 6px rgba(0,0,0,.2)}
.slide{left:70px;top:207px;width:769px;height:236px;border-radius:8px;background:linear-gradient(120deg,#777,#d8d8d8 45%,#f4f4f4 70%,#9a9a9a)}
.card{top:456px;width:152px;height:90px;background:var(--orange);border-radius:8px;color:#fff;font-size:13px;text-align:center;padding-top:6px}
.card .ph{position:absolute;left:5px;top:23px;width:142px;height:62px;border-radius:6px;background:linear-gradient(#dcdcdc,#a8a8a8)}
.content{left:56px;top:574px;width:796px;height:414px;background:var(--white);border-radius:6px}
.h2{font-family:"Open Sans",sans-serif;font-size:22px;color:#111}
.project{left:64px;width:472px;height:114px;border:1px solid var(--line);background:var(--white)}
.thumb{position:absolute;left:11px;top:11px;width:123px;height:93px;border:2px solid #ddd;background:linear-gradient(#eee 0 20%,#7b8a72 20% 80%,#eee 80%)}
.ptext{position:absolute;left:145px;top:10px;font-size:11px;line-height:13px;width:240px}
.ptitle{color:var(--orange-text);font-weight:700;font-size:12px}
.stars{margin:6px 0 6px;display:flex;gap:3px}
.stars b{width:11px;height:11px;background:#5fb3e8;clip-path:polygon(50% 0,63% 35%,100% 38%,70% 60%,80% 100%,50% 76%,20% 100%,30% 60%,0 38%,37% 35%)}
.launch{color:var(--orange-text);font-weight:700}
.blogs{left:546px;top:581px;width:300px;height:398px;background:var(--blogbox);border-radius:8px}
.post{position:absolute;left:7px;width:284px;font-size:10.5px;line-height:12px;color:#222}
.post .t{color:var(--orange-text);font-weight:700;font-size:11px}
.post .m{color:var(--muted);margin-bottom:12px}
.rule{position:absolute;left:7px;width:284px;border-top:1px solid #bdbdb8}
.more{left:822px;top:958px;color:var(--orange-text);font-size:10px;font-weight:700}
.footer{left:0;top:1010px;width:906px;height:142px;background:var(--dark)}
.fcol{top:1020px;color:#ddd;font-family:"Open Sans",sans-serif;font-size:11px;line-height:16.3px}
.fcol h3{font-weight:400;font-size:13px;color:#fff;border-bottom:1px solid #5a5a5a;padding-bottom:4px;margin-bottom:10px;width:170px}
.fsep{top:1020px;width:1px;height:120px;background:#b5481a}
.legal{left:0;top:1152px;width:906px;height:28px;background:var(--orange);color:#fff;font-family:"Open Sans",sans-serif;font-size:9px}
.legal .big{font-size:19px;position:absolute;left:418px;top:1px}
.base{left:0;top:1180px;width:906px;height:20px;background:var(--topbar)}
</style>
</head>
<body>
<div class="abs topbar">
  <span style="left:78px">www.northsurveyhost.ca</span>
  <span style="left:238px">|</span>
  <span style="left:257px">capitalsitecraft.ca</span>
  <span style="left:525px">Contact us today -</span>
  <span class="phone" style="left:622px">613-555-0142</span>
  <span style="left:713px">|</span>
  <span style="left:728px">sales@brindlecove.ca</span>
</div>
<div class="abs header"></div>
<div class="abs logo"><div class="logo-mark"></div><div class="logo-name">Brindlecove<br>Communications</div></div>
<div class="abs quote"><i>?</i>Request a Quote</div>
<div class="abs social" style="left:808px"></div>
<div class="abs social" style="left:828px;background:#3fb6e6"></div>

<div class="abs band"></div>
<nav class="abs nav">
  <span class="on" style="left:30px">Home</span><span style="left:86px">|</span>
  <span style="left:117px">Web design</span><span style="left:208px">|</span>
  <span style="left:240px">Mobile Apps</span><span style="left:334px">|</span>
  <span style="left:355px">Custom Software</span><span style="left:473px">|</span>
  <span style="left:502px">Accessible</span><span style="left:591px">|</span>
  <span style="left:618px">CMS</span><span style="left:670px">|</span>
  <span style="left:696px">Contact us</span>
</nav>

<div class="abs tab on" style="left:72px;width:132px">Our Vision</div>
<div class="abs tab" style="left:210px;width:128px">Business</div>
<div class="abs tab" style="left:346px;width:128px">Government</div>
<div class="abs tab" style="left:484px;width:178px">Associations / Non-profit</div>
<div class="abs stage"></div>
<div class="abs slide" role="img" aria-label="Black and white photo of hands writing on a document with a pen"></div>

<div class="abs card" style="left:60px">Web design<div class="ph" role="img" aria-label="Photo of a thoughtful businesswoman"></div></div>
<div class="abs card" style="left:218px">Mobile Apps<div class="ph" role="img" aria-label="Photo of a woman talking on a phone"></div></div>
<div class="abs card" style="left:377px">Custom Software<div class="ph" role="img" aria-label="Photo of a business team"></div></div>
<div class="abs card" style="left:535px">Accessible<div class="ph" role="img" aria-label="Photo of a man working at a laptop"></div></div>
<div class="abs card" style="left:693px">CMS<div class="ph" role="img" aria-label="Photo of hands typing on a laptop"></div></div>

<div class="abs content"></div>
<div class="abs h2" style="left:71px;top:587px">Feature Projects</div>
<div class="abs project" style="top:617px"><div class="thumb" role="img" aria-label="Screenshot of a project website"></div><div class="ptext"><div class="ptitle">Professional Design</div>We can help to give you the professional image that you want to present to visitors.<div class="stars"><b></b><b></b><b></b><b></b><b></b></div><div class="launch">Lanch Project</div></div></div>
<div class="abs project" style="top:736px"><div class="thumb" role="img" aria-label="Screenshot of a project website"></div><div class="ptext"><div class="ptitle">Professional Design</div>We can help to give you the professional image that you want to present to visitors.<div class="stars"><b></b><b></b><b></b><b></b><b></b></div><div class="launch">Lanch Project</div></div></div>
<div class="abs project" style="top:855px"><div class="thumb" role="img" aria-label="Screenshot of a project website"></div><div class="ptext"><div class="ptitle">Professional Design</div>We can help to give you the professional image that you want to present to visitors.<div class="stars"><b></b><b></b><b></b><b></b><b></b></div><div class="launch">Lanch Project</div></div></div>

<div class="abs blogs">
  <div class="h2" style="position:absolute;left:7px;top:7px">Blogs</div>
  <div class="post" style="top:46px"><div class="t">25 Outstanding Minimalist Website Designs</div><div class="m">Published December 20th, 2011 in Galleries - 9 Comments</div>Minimalism is popular with many designers, primarily because the lack of clutter can help to create a positive user experience. While it is not a style that works in all situations (and what style does?), minimalism can be extremely effective when it is done effectively. It would seem that minimal websites would be easy to design due to the lack of excess, but achieving a high-quality minimal design can prove to be more difficult than expected. In this post we'll provide some inspiration for you own work by showcasing 25 beautiful, minimal websites.</div>
  <div class="rule" style="top:208px"></div>
  <div class="post" style="top:223px;left:10px"><div class="t">25 Outstanding Minimalist Website Designs</div><div class="m">Published December 20th, 2011 in Galleries - 9 Comments</div>Minimalism is popular with many designers, primarily because the lack of clutter can help to create a positive user experience. While it is not a style that works in all situations (and what style does?), minimalism can be extremely effective when it is done.</div>
  <div class="rule" style="top:326px"></div>
</div>
<div class="abs more">&gt;&gt;</div>

<div class="abs footer"></div>
<div class="abs fcol" style="left:64px"><h3>Web design</h3>On-line brochure sites<br>Content sites<br>Lead-generation sites<br>E-commerce sites<br>Self-service sites</div>
<div class="abs fsep" style="left:254px"></div>
<div class="abs fcol" style="left:282px"><h3>Mobile Apps</h3>Bookmarking<br>Miscellaneous<br>Publishing<br>Search</div>
<div class="abs fsep" style="left:455px"></div>
<div class="abs fcol" style="left:483px"><h3>Accessible</h3>PDF<br>HTML</div>
<div class="abs fsep" style="left:640px"></div>
<div class="abs fcol" style="left:674px"><h3>CMS</h3>Lumen<br>Tessera</div>

<div class="abs legal">
  <span style="position:absolute;left:12px;top:10px">Copyright © 2011 - Brindlecove Communications - 14 Larkspur Lane, Ottawa ON, K1X 0B4</span>
  <span class="big">(613) 555-0142</span>
  <span style="position:absolute;left:717px;top:8px">Privacy Statement &nbsp; | &nbsp; Terms &amp; Conditions</span>
</div>
<div class="abs base"></div>
</body>
</html>
```